Website for Wedding Cake Business based in Suffolk countryside

I need a website to advertise my services. I bake wedding cakes and celebration cakes. My style of baking is very rustic and I use lots of local and homegrown ingredients within my baking. I’d like the website to be classy but countryside chic. I want to website to reflect quality and sophistication but also keep the countryside vibe. My logo is currently a mustard yellow and grey but this may be changed so the colour palette is completely open.

Target Market(s)

Couples and women aged 21-40

Industry/Entity Type

Wedding

Number of Pages Required

4 page

Colors

Designer to choose colors to be used in the design.

Requirements
Must have
• Must appeal to men and women. Must have a contact button, social media links, price list and photo gallery.
• Functioning drop downs (price list, gallery, booking form)
Nice to have
• Very simple layout with menu bar across the top of the page. A section can update which shows which feeding Faye or show I’ll be a next with a map.
Should not have
• Nothing to bold, block coloured or cheesy.

```html
<!DOCTYPE html>
<html lang="en">
<head>
<meta charset="utf-8">
<title>Hazelcroft – Contact Us</title>
<link href="https://fonts.googleapis.com/css2?family=Open+Sans:wght@400;600;700&family=Pacifico&display=swap" rel="stylesheet">
<style>
  :root {
    --ink: #4a2c2a;
    --text: #2b2b2b;
    --muted: #7a7a7a;
    --line: #e6e6e6;
    --field-border: #cfcfcf;
    --nav-bg: #e1eaf4;
    --topbar-bg: #f4f5f6;
    --accent-pink: #fcdcd6;
    --map-tone: #eeeeea;
    --white: #ffffff;
  }
  * { box-sizing: border-box; margin: 0; padding: 0; }
  html, body { width: 960px; height: 1200px; overflow: hidden; }
  body {
    position: relative;
    background: var(--white);
    font-family: "Open Sans", Arial, sans-serif;
    color: var(--text);
  }
  .abs { position: absolute; }

  /* Announcement bar */
  .announce {
    left: 0; top: 0; width: 960px; height: 26px;
    background: var(--topbar-bg);
    border-top: 2px solid var(--accent-pink);
    font-size: 8.5px; letter-spacing: 1px; text-transform: uppercase;
    color: #555; display: flex; align-items: center; justify-content: center;
  }
  .announce strong { color: #333; margin-left: 4px; text-decoration: underline; font-weight: 700; }
  .announce-close { position: absolute; right: 108px; top: 5px; font-size: 12px; color: #555; }

  /* Brand */
  .brand {
    left: 0; top: 38px; width: 960px; text-align: center;
  }
  .brand-mark { display: inline-flex; align-items: center; gap: 8px; }
  .brand-square { width: 10px; height: 10px; background: var(--ink); }
  .brand-name {
    font-size: 22px; font-weight: 600; letter-spacing: 2px; color: var(--ink);
  }
  .brand-tagline { font-size: 7px; font-weight: 600; color: var(--text); margin-top: 8px; letter-spacing: .5px; }

  /* Navigation */
  .main-nav {
    left: 0; top: 131px; width: 960px; height: 39px; background: var(--nav-bg);
  }
  .main-nav a {
    position: absolute; top: 12px; transform: translateX(-50%);
    font-size: 11px; font-weight: 600; letter-spacing: 1.5px; color: #3a3a3a; text-decoration: none;
  }

  /* Page title */
  .page-title {
    left: 0; top: 202px; width: 960px; text-align: center;
    font-family: "Pacifico", cursive; font-size: 34px; color: var(--ink); font-weight: 400;
  }
  .title-ornament {
    left: 445px; top: 270px; width: 69px; height: 11px; background: #d9cfcd; border-radius: 6px;
  }

  /* Contact form */
  .field-label { left: 99px; font-size: 14.5px; font-weight: 700; color: var(--ink); letter-spacing: .3px; }
  .field-box { left: 99px; width: 372px; border: 1px solid var(--field-border); background: var(--white); }
  .submit-btn {
    left: 99px; top: 759px; width: 111px; height: 39px; background: var(--accent-pink);
    font-size: 14px; font-weight: 700; letter-spacing: 1px; color: var(--ink);
    display: flex; align-items: center; justify-content: center; border: none;
  }

  /* Map & info */
  .location-map { left: 490px; top: 322px; width: 370px; height: 227px; background: var(--map-tone); }
  .info-heading { left: 489px; top: 574px; font-size: 14.5px; font-weight: 700; color: #111; }
  .info-row { left: 489px; width: 380px; display: flex; font-size: 10px; line-height: 15.5px; color: #222; }
  .info-row dt { width: 57px; font-weight: 700; font-size: 11px; color: #111; }

  /* Footer */
  .footer-rule { left: 0; top: 861px; width: 960px; height: 1px; background: var(--line); }
  .footer-brand { left: 99px; top: 916px; width: 105px; text-align: center; }
  .footer-brand .brand-name { font-size: 13px; letter-spacing: 1px; }
  .footer-brand .brand-square { width: 7px; height: 7px; }
  .footer-brand .brand-mark { gap: 5px; }
  .footer-brand .brand-tagline { font-size: 6px; margin-top: 8px; }
  .footer-col { top: 905px; }
  .footer-col h4 { font-size: 10.5px; font-weight: 700; letter-spacing: .8px; color: #111; margin-bottom: 9px; }
  .footer-col li { list-style: none; font-size: 10px; line-height: 15.6px; color: #222; }
  .social { left: 622px; top: 1051px; display: flex; gap: 23px; }
  .social span { width: 12px; height: 12px; border-radius: 50%; background: #3a3a3a; display: block; }
  .bottom-rule { left: 0; top: 1131px; width: 960px; height: 1px; background: var(--line); }
  .copyright { left: 0; top: 1158px; width: 960px; text-align: center; font-size: 9px; color: var(--muted); letter-spacing: .3px; }
</style>
</head>
<body>

  <div class="abs announce">Free delivery on orders over $50. <strong>Shop now</strong>
    <span class="announce-close">×</span>
  </div>

  <header class="abs brand">
    <div class="brand-mark"><span class="brand-square"></span><span class="brand-name">HAZELCROFT</span></div>
    <div class="brand-tagline">Coffee and Bakehouse</div>
  </header>

  <nav class="abs main-nav">
    <a href="#" style="left:296px">HOME</a>
    <a href="#" style="left:412px">INFORMATION</a>
    <a href="#" style="left:529px">GALLERY</a>
    <a href="#" style="left:641px">CONTACT US</a>
  </nav>

  <h1 class="abs page-title">Contact Us</h1>
  <div class="abs title-ornament" role="img" aria-label="Small decorative flourish with a chef's hat"></div>

  <form>
    <label class="abs field-label" style="top:319px">Name</label>
    <div class="abs field-box" style="top:347px;height:39px"></div>
    <label class="abs field-label" style="top:404px">Email</label>
    <div class="abs field-box" style="top:433px;height:38px"></div>
    <label class="abs field-label" style="top:489px">Phone Number</label>
    <div class="abs field-box" style="top:518px;height:38px"></div>
    <label class="abs field-label" style="top:574px">Message</label>
    <div class="abs field-box" style="top:603px;height:121px"></div>
    <button class="abs submit-btn" type="button">SUBMIT</button>
  </form>

  <div class="abs location-map" role="img" aria-label="Road map showing the bakehouse location and surrounding towns"></div>

  <h3 class="abs info-heading">Contact Info</h3>
  <dl>
    <div class="abs info-row" style="top:614px"><dt>Address:</dt><dd>134 Lorem Ipsum Dolor Sit,<br>ndw, 2564, Country</dd></div>
    <div class="abs info-row" style="top:659px"><dt>Phone:</dt><dd>+610 987 654 3210</dd></div>
    <div class="abs info-row" style="top:692px"><dt>Email:</dt><dd>hello@hazelcroft.com</dd></div>
  </dl>

  <div class="abs footer-rule"></div>

  <div class="abs footer-brand">
    <div class="brand-mark"><span class="brand-square"></span><span class="brand-name">HAZELCROFT</span></div>
    <div class="brand-tagline">Coffee and Bakehouse</div>
  </div>

  <div class="abs footer-col" style="left:253px">
    <h4>CATEGORIES</h4>
    <ul>
      <li>Edibles</li><li>Tools</li><li>Weeding Cake</li><li>Birthday Cake</li><li>Party Cake</li>
      <li>Anniversary Cake</li><li>Decorations</li><li>Colours</li><li>Boards &amp; Boxes</li><li>Sale</li>
    </ul>
  </div>

  <div class="abs footer-col" style="left:425px">
    <h4>USEFUL LINKS</h4>
    <ul>
      <li>About us</li><li>Cake Gallery</li><li>Our Brands</li><li>Delivery</li><li>Support</li><li>Contact Us</li>
    </ul>
  </div>

  <div class="abs footer-col" style="left:620px">
    <h4>CONTACT US</h4>
    <ul>
      <li>hazelcroft</li><li>134 Lorem Ipsum Dolor Sit,</li><li>ndw, 2564</li><li>Country</li>
      <li>&nbsp;</li><li>+610 987 654 3210</li>
    </ul>
  </div>

  <div class="abs social">
    <span aria-label="Social link 1"></span>
    <span aria-label="Social link 2"></span>
    <span aria-label="Social link 3"></span>
    <span aria-label="Social link 4"></span>
  </div>

  <div class="abs bottom-rule"></div>
  <p class="abs copyright">© 2019 &nbsp;Hazelcroft. All rights reserved.</p>

</body>
</html>
```